Manufacturer's Representative Group needs a clean new Website

We represent and sell a number of suppliers that design and build products used in Biopharmaceutical manufacturing. Our sales region is in the central US. Our customer base is scientific / engineering based - so clean, we organized design with a focus on the products - easy and clear navigation is necessary. We do not sell direct or warehouse product - so e-commerce is not needed. Our customers will use the website for reference on what we do and offer - we will use the site as a platform to present products from each vendor and the home page will be used to capture an overview and draw users deeper into the site. You can view our current site - which needs A LOT of help to get ideas on products represented and types of products

Target Market(s)

Engineers and Pharmaceutical / Bio pharm end users

Industry/Entity Type

E-Commerce

Number of Pages Required

2 page

Font styles to use
Sans Serif

Requirements
Must have
• I need a home page that provides a snapshot of my company and the product lines we represent - then a second page that I can copy as a template for each line I rep as well as for an "About us / contact" page.
• I would like to be able to manage content on the pages so something easy to adjust pictures or add content is a must
• Must use our logo

```html
<!DOCTYPE html>
<html lang="en">
<head>
<meta charset="utf-8">
<title>Prairie Bio — Home</title>
<link rel="stylesheet" href="https://fonts.googleapis.com/css2?family=Montserrat:wght@500;600;700&family=Arimo:wght@400;700&display=swap">
<style>
  :root{
    --navy:#27205e;
    --orange:#f05a28;
    --page:#f4f4f4;
    --panel:#e4e4e4;
    --rule:#d6d6d6;
    --text:#2b2b2b;
    --muted:#555;
    --white:#ffffff;
    --button:#4a2aa3;
  }
  *{box-sizing:border-box;margin:0;padding:0}
  html,body{width:1106px;height:1200px;overflow:hidden;background:var(--page)}
  body{position:relative;font-family:"Arimo",Arial,sans-serif;color:var(--text)}
  .heading{font-family:"Montserrat",Arial,sans-serif;font-weight:600;letter-spacing:.5px;color:#333}
  .accent{color:var(--orange)}

  .brand{position:absolute;left:92px;top:30px;display:flex;align-items:center;gap:14px}
  .brand-dot{width:30px;height:30px;border-radius:50%;background:var(--orange)}
  .brand-name{font-family:"Montserrat",sans-serif;font-weight:500;font-size:40px;color:var(--navy);letter-spacing:-.5px}

  .header-rule{position:absolute;left:0;right:0;top:102px;border-top:1px solid var(--rule)}
  .main-nav{position:absolute;left:676px;top:94px;display:flex;gap:0;background:var(--page);padding:0 14px}
  .main-nav a{font-size:13.5px;color:#444;text-decoration:none;letter-spacing:.4px;margin-right:47px;position:relative}
  .main-nav a:last-child{margin-right:0}
  .main-nav .current svg{position:absolute;left:50%;top:17px;margin-left:-6px}

  .hero{position:absolute;left:99px;top:134px;width:908px;height:345px;
    background:linear-gradient(100deg,#c9d6ea 0%,#e7eef7 25%,#7e9fd0 38%,#dfe3ea 55%,#c1a9b0 68%,#a7acb8 85%,#d8dde6 100%)}

  .about{position:absolute;left:94px;top:510px;width:620px}
  .about h2{font-size:20px}
  .about p{margin-top:18px;font-size:11.5px;line-height:18.4px;padding-left:1px}
  .section-rule{position:absolute;left:92px;top:685px;width:620px;border-top:1px solid var(--rule)}

  .products{position:absolute;left:92px;top:712px;width:630px}
  .products h2{font-size:20px}
  .products .lead{margin-top:8px;font-size:13px;color:var(--orange)}
  .product-card{position:absolute;top:63px;width:196px;height:149px;overflow:hidden}
  .product-card .photo{position:absolute;inset:0}
  .product-card .label{position:absolute;left:0;right:0;bottom:0;height:33px;background:var(--navy);color:var(--white);
    font-family:"Montserrat",sans-serif;font-weight:500;font-size:17px;letter-spacing:1.4px;line-height:35px;padding-left:16px}

  .cta{position:absolute;left:752px;top:510px;width:257px;height:414px;background:var(--panel);padding:10px 13px 0}
  .cta h2{font-size:22px;padding-bottom:7px;border-bottom:1px dotted #aaa}
  .cta p{margin-top:11px;font-size:11.5px;line-height:16.6px;color:#444}
  .field{display:block;margin-top:12px;height:34px;border-radius:17px;background:var(--white);
    border:1px solid #d2d2d2;box-shadow:inset 0 2px 3px rgba(0,0,0,.08);font-size:11.5px;color:#444;padding:10px 16px}
  .field.tall{height:76px;border-radius:20px;margin-left:4px;margin-top:18px;padding-top:15px}
  .submit{position:absolute;right:28px;top:366px;width:102px;height:33px;border-radius:12px;border:2px solid var(--white);
    background:linear-gradient(#5b3bc2,var(--button));color:var(--white);font-size:12px;font-weight:700;text-align:center;line-height:29px;
    box-shadow:0 0 0 1px #c6c6c6}

  .partners{position:absolute;left:92px;top:961px;width:922px;height:123px;background:var(--white);border:1px solid #e6e6e6}
  .partners h2{text-align:center;margin-top:12px;font-size:21px;color:#333}
  .partner-list{display:flex;justify-content:space-between;align-items:center;padding:0 30px;margin-top:24px}
  .partner{font-family:"Montserrat",sans-serif;font-weight:600;font-size:17px;color:#4a5a78}

  .footer{position:absolute;left:0;top:1108px;width:1106px;height:92px;background:var(--navy);border-top:4px solid var(--orange)}
  .footer-nav{position:absolute;left:99px;top:20px;font-size:14px;color:var(--white)}
  .footer-nav span{margin:0 20px}
  .copyright{position:absolute;left:99px;top:46px;font-size:14px;color:var(--white)}
  .footer-brand{position:absolute;left:760px;top:20px;display:flex;align-items:center;gap:12px}
  .footer-brand .brand-dot{width:26px;height:26px;background:var(--white)}
  .footer-brand .brand-name{font-size:30px;color:var(--white)}
</style>
</head>
<body>
  <header>
    <div class="brand"><span class="brand-dot"></span><span class="brand-name">Prairie Bio</span></div>
    <div class="header-rule"></div>
    <nav class="main-nav">
      <a href="#" class="current">HOME<svg width="12" height="8" viewBox="0 0 12 8"><path d="M1 1l5 5 5-5" fill="none" stroke="#f05a28" stroke-width="2.5"/></svg></a>
      <a href="#">CONTACT</a>
      <a href="#">PRODUCTS</a>
    </nav>
  </header>

  <div class="hero" role="img" aria-label="Cleanroom staff in protective suits working beside a stainless steel bioreactor and fluid vessels"></div>

  <section class="about">
    <h2 class="heading">ABOUT <span class="accent">PRAIRIE BIO</span></h2>
    <p>Prairie Biosolutions is a distribution channel, licensed partner and manufacturers representative group provid-<br>ing high quality fluid handling products and technical services to the Midwestern biopharmaceutical community.<br>With a core staff of experienced professionals and a team approach to all customer needs,<br><br>we offer over 30 years of cGMP experience in the selection and use of most process consumable products.<br>We're looking forward to working with you</p>
  </section>
  <div class="section-rule"></div>

  <section class="products">
    <h2 class="heading">OUR PRODUCTS</h2>
    <p class="lead">Click on any of the product logos below to be directed to a page specific to that line</p>
    <a class="product-card" style="left:3px">
      <div class="photo" role="img" aria-label="Silicone tubing assemblies and fittings on a blue backdrop" style="background:radial-gradient(circle at 60% 40%,#8fa6c8,#2a3f78 60%,#101a3a)"></div>
      <div class="label">LOREM IPSUM</div>
    </a>
    <a class="product-card" style="left:220px">
      <div class="photo" role="img" aria-label="Blue peristaltic pump with digital display" style="background:linear-gradient(160deg,#8fb8e2,#2d5ea8 55%,#b8c4cf)"></div>
      <div class="label">LOREM IPSUM</div>
    </a>
    <a class="product-card" style="left:430px">
      <div class="photo" role="img" aria-label="Red peristaltic pump with tubing head" style="background:linear-gradient(160deg,#d84040,#b01f24 55%,#e8e0cc)"></div>
      <div class="label">LOREM IPSUM</div>
    </a>
  </section>

  <aside class="cta">
    <h2 class="heading"><span class="accent">CALL TO</span> ACTION</h2>
    <p>In hac habitasse platea dictumst. Donec com-modo, purus sit amet luctus placerat, nunc nulla congue enim, vitae vulputate mauris ligula nec orci.</p>
    <div class="field">Your Name</div>
    <div class="field">Your Email</div>
    <div class="field">Your Phone</div>
    <div class="field tall">Additional Information</div>
    <div class="submit">Submit Form</div>
  </aside>

  <section class="partners">
    <h2 class="heading">Companies Represented</h2>
    <div class="partner-list">
      <span class="partner">Norvale Polymers</span>
      <span class="partner">Tubelink USA</span>
      <span class="partner">Fluvora</span>
      <span class="partner">Caldris</span>
      <span class="partner">Purelock</span>
      <span class="partner">Modara</span>
    </div>
  </section>

  <footer class="footer">
    <div class="footer-nav">Home<span>|</span>Contact Us<span>|</span>Products</div>
    <div class="copyright">© Prairie Biosolutions, Corp.</div>
    <div class="footer-brand"><span class="brand-dot"></span><span class="brand-name">Prairie Bio</span></div>
  </footer>
</body>
</html>
```